Design of a Web Development Agency

We're a web development agency (we do not offer design services). We'd like to get a new website up and running. We do custom web application development - large scale applications in the financial, healthcare, automotive, and other industries.

We need the following types of pages designed:
1) Homepage
2) Blog
3) Services page
4) Packages page
4) Generic content
5) Contact Us form.

The design should be consistent with our current icon. We're looking for a clean, corporate, brand. We'd like the design to expand on the concepts in the logo - the use of the electrical wiring motif / the colors / etc.

We offer the following services: 1) Corvel web hosting consulting, 2) custom application development, 3) eVN development, 4) Quillset development.

We offer packages in numbers of hours. We have about 3-4 tiers of services - the number of hours versus the monthly invoice total. For example, 5 hours per month of $500.00, for example.

Target Market(s)

Corporate clients

Industry/Entity Type

Electrical

Colors
acd036
33b7a4
33a6d7
3176b5
876aae
b768aa
fbee3e

Requirements
Must have
• Responsive / mobile friendly design.
• An email submitting form on the contact us page
Nice to have
• We'd like a bit of San Francisco to come through (where we're located)
• A plimbo map of our address on the contact us page
Should not have
• Excessive imagery. We don't have a lot of imagery, so we'd basically have to go out and find stock photography to put in it's place, which we just don't really want to do. All imagery should be supplied by the designer (we'll pay any copyright fees, if applicable, you just have to send us a list of the links to the imagery. Max budget would be $100-$200 on imagery, but preferably as little as possible).

```html
<!DOCTYPE html>
<html lang="en">
<head>
<meta charset="utf-8">
<title>Halvern Web Works</title>
<link href="https://fonts.googleapis.com/css2?family=Open+Sans:wght@400;600;700&display=swap" rel="stylesheet">
<style>
:root{
  --green:#7bb12b;
  --green-dark:#5f9226;
  --nav:#555555;
  --pink:#b768aa;
  --purple:#876aae;
  --blue:#3176b5;
  --sky:#33a6d7;
  --heading:#1f6fb2;
  --news:#1a6fa8;
  --text:#666;
  --footer:#2b2b2b;
  --footer-base:#1e1e1e;
  --footer-text:#9a9a9a;
}
*{margin:0;padding:0;box-sizing:border-box}
html,body{width:885px;height:1200px;overflow:hidden;background:#fff;font-family:'Open Sans',Arial,sans-serif}
.page{position:relative;width:885px;height:1200px}
.abs{position:absolute}
.brand{left:105px;top:17px;display:flex;align-items:center;gap:10px}
.brand-mark{width:48px;height:48px;border-radius:50%;background:#c9d83a;border:3px solid #333}
.brand-name{font-size:13px;color:#222;letter-spacing:.2px}
.search{left:607px;top:32px;width:174px;height:23px;border:1px solid #ddd;border-radius:4px;background:#f4f4f4;overflow:hidden}
.search-btn{position:absolute;right:0;top:0;width:24px;height:23px;background:var(--green)}
.nav{left:0;top:88px;width:885px;height:48px;background:var(--nav)}
.nav-item{position:absolute;top:0;height:48px;line-height:48px;color:#fff;font-size:11px;transform:translateX(-50%)}
.nav-home{left:104px;width:76px;background:var(--green);text-align:center;transform:none}
.hero{left:0;top:136px;width:885px;height:326px;background:linear-gradient(180deg,#0e1a3e 0%,#1b2c5e 55%,#2a2848 75%,#141826 100%)}
.dots{left:401px;top:382px;display:flex;gap:6px}
.dot{width:8px;height:8px;border-radius:50%;background:#bbb}
.dot.on{background:#fff;border:2px solid var(--green)}
.strip{left:0;top:405px;width:885px;height:57px;background:#1f2126}
.tagline{left:230px;top:405px;width:425px;height:57px;background:var(--green-dark);color:#fff;font-size:11.5px;font-weight:600;text-align:center;line-height:57px}
.arrow{top:424px}
.services{left:104px;top:483px;width:677px;height:194px;display:flex}
.svc{flex:1;padding:12px 10px;color:#fff}
.svc h3{font-weight:400;font-size:13px;line-height:23px;text-transform:uppercase;margin-bottom:9px}
.svc p{font-size:9.3px;line-height:16px}
.svc a{display:block;margin-top:9px;font-size:10.5px;font-weight:600;color:#fff;text-decoration:underline}
.about-title{left:0;top:694px;width:885px;text-align:center;color:var(--heading);font-size:15px;font-weight:600}
.about-rule{left:288px;top:726px;width:310px;height:1px;background:#e2e2e2}
.about-rule-accent{left:404px;top:726px;width:70px;height:1px;background:var(--heading)}
.diamond{left:435px;top:723px;width:7px;height:7px;background:var(--heading);transform:rotate(45deg)}
.about-text{left:110px;top:748px;width:665px;text-align:center;font-size:9.2px;line-height:16.5px;color:var(--text)}
.testi-title{left:104px;top:818px;color:var(--heading);font-size:14px;font-weight:600}
.testi-rule{left:104px;top:844px;width:436px;height:1px;background:#ddd}
.pager{top:825px;width:12px;height:12px;border-radius:50%;background:#555}
.portrait{left:104px;top:857px;width:161px;height:103px;border:1px solid #ddd;background:linear-gradient(180deg,#f3f1ee,#d8d2cc)}
.testi-text{left:271px;top:856px;width:270px;font-family:Arial,sans-serif;font-size:8px;line-height:12.5px;color:#333;text-align:justify}
.testi-text p+p{margin-top:12px}
.testi-name{left:274px;top:942px;font-family:Arial,sans-serif;font-size:9px;color:var(--heading)}
.news{left:565px;top:821px;width:216px;height:126px;background:var(--news);color:#fff}
.news h4{font-size:11px;font-weight:600;padding:8px 0 0 15px;height:30px;border-bottom:1px solid #2f80b8}
.news label{display:block;font-size:7px;font-weight:600;margin:10px 0 0 17px}
.news-field{position:absolute;left:15px;top:59px;width:192px;height:20px;background:#e8e8e8}
.news-btn{position:absolute;left:153px;top:94px;width:54px;height:20px;background:#f2f2f2;color:#222;font-size:8.5px;font-weight:700;text-align:center;line-height:20px}
.footer{left:0;top:991px;width:885px;height:166px;background:var(--footer)}
.footer-base{left:0;top:1157px;width:885px;height:43px;background:var(--footer-base)}
.col-title{top:1010px;color:#ddd;font-size:11px}
.col-list{top:1035px;list-style:none;font-size:8px;color:var(--footer-text);line-height:18.8px;text-transform:uppercase}
.divider{top:1011px;width:1px;height:134px;background:#444}
.contact-copy{left:411px;top:1036px;width:210px;font-size:8.5px;line-height:17.5px;color:#777;text-transform:uppercase}
.contact-lines{left:411px;top:1093px;font-size:8px;line-height:19px;color:var(--footer-text)}
.contact-lines b{color:#ddd;font-weight:400}
.social{left:692px;top:1032px;list-style:none}
.social li{display:flex;align-items:center;gap:10px;height:25.6px;font-size:8.5px;color:var(--footer-text)}
.social li span{width:20px;height:20px;border-radius:50%;background:#eee}
.copyright{left:105px;top:1173px;font-size:8px;color:#999}
</style>
</head>
<body>
<div class="page">
  <div class="abs brand"><div class="brand-mark"></div><span class="brand-name">HALVERN WEB WORKS</span></div>
  <div class="abs search"><div class="search-btn">
    <svg width="24" height="23" viewBox="0 0 24 23"><circle cx="11" cy="10" r="3.5" fill="none" stroke="#fff" stroke-width="1.6"/><line x1="13.5" y1="12.5" x2="17" y2="16" stroke="#fff" stroke-width="2"/></svg>
  </div></div>

  <nav class="abs nav">
    <span class="nav-item nav-home">HOME</span>
    <span class="nav-item" style="left:264px">ABOUT US</span>
    <span class="nav-item" style="left:374px">BLOG</span>
    <span class="nav-item" style="left:486px">SERVICES</span>
    <span class="nav-item" style="left:611px">PACKAGES</span>
    <span class="nav-item" style="left:745px">CONTACT US</span>
  </nav>

  <div class="abs hero" role="img" aria-label="Night photograph of an illuminated arch bridge over a river"></div>
  <div class="abs dots"><span class="dot on"></span><span class="dot"></span><span class="dot"></span><span class="dot"></span></div>
  <div class="abs strip"></div>
  <div class="abs tagline">BUILDING A CLOUD APPLICATION SO SOLID, YOU CAN'T FALL THROUGH IT</div>
  <svg class="abs arrow" style="left:198px" width="14" height="18" viewBox="0 0 14 18"><polyline points="10,2 3,9 10,16" fill="none" stroke="#ddd" stroke-width="3"/></svg>
  <svg class="abs arrow" style="left:668px" width="14" height="18" viewBox="0 0 14 18"><polyline points="4,2 11,9 4,16" fill="none" stroke="#ddd" stroke-width="3"/></svg>

  <section class="abs services">
    <div class="svc" style="background:var(--pink)"><h3>Corvel web hosting consulting</h3><p>Sed ut perspiciatis unde omnis iste natus error sit voluptatem accusantium totam remaperiam, eaque ipsa quae ab illo inven-tore veritatis et ...</p><a>Read More</a></div>
    <div class="svc" style="background:var(--purple)"><h3>Custom application development</h3><p>Sed ut perspiciatis unde omnis iste natus error sit voluptatem accusantium totam remaperiam, eaque ipsa quae ab illo inven-tore veritatis et ...</p><a>Read More</a></div>
    <div class="svc" style="background:var(--blue)"><h3>eVN<br>development</h3><p>Sed ut perspiciatis unde omnis iste natus error sit voluptatem accusantium totam remaperiam, eaque ipsa quae ab illo inven-tore veritatis et ...</p><a>Read More</a></div>
    <div class="svc" style="background:var(--sky)"><h3>Quillset<br>development.</h3><p>Sed ut perspiciatis unde omnis iste natus error sit voluptatem accusantium totam remaperiam, eaque ipsa quae ab illo inven-tore veritatis et ...</p><a>Read More</a></div>
  </section>

  <h2 class="abs about-title">ABOUT US</h2>
  <div class="abs about-rule"></div><div class="abs about-rule-accent"></div><div class="abs diamond"></div>
  <p class="abs about-text">Sed ut perspiciatis unde omnis iste natus error sit voluptatem accusantium doloremque laudantium, totam rem aperiam, eaque ipsa quae ab illo inventore veritatis et quasi architecto beatae vitae dicta sunt explicabo.Nemo enim ipsam voluptatem quia voluptas sit aspernatur aut odit aut fugit, tempora incidunt ut labore et dolore magnam aliquam quaerat voluptatem.</p>

  <h2 class="abs testi-title">TESTIMONIALS</h2>
  <div class="abs testi-rule"></div>
  <svg class="abs pager" style="left:510px" width="12" height="12" viewBox="0 0 12 12"><polyline points="7,3 4,6 7,9" fill="none" stroke="#fff" stroke-width="1.6"/></svg>
  <svg class="abs pager" style="left:525px" width="12" height="12" viewBox="0 0 12 12"><polyline points="5,3 8,6 5,9" fill="none" stroke="#fff" stroke-width="1.6"/></svg>
  <div class="abs portrait" role="img" aria-label="Portrait photo of a smiling client in a suit"></div>
  <div class="abs testi-text">
    <p>Neque porro quisquam est, qui dolorem ipsum quia dolor sit amet, consectetur, adipisci velit, sed quia non numquam eius modi tempora incidunt ut labore et dolore magnam aliquam quaerat voluptatem.</p>
    <p>Ut enim ad minima veniam, quis nostrum exercitationem ullam corporis suscipit laboriosam, nisi ut aliquid ex ea commodi consequatur?</p>
  </div>
  <span class="abs testi-name">esse quam</span>

  <form class="abs news">
    <h4>SIGN UP FOR OUR EMAIL NEWSLETTER</h4>
    <label>YOUR EMAIL ADDRESS*</label>
    <div class="news-field"></div>
    <div class="news-btn">SUBMIT</div>
  </form>

  <footer>
    <div class="abs footer"></div>
    <h5 class="abs col-title" style="left:105px;font-weight:400">TEXT LINKS</h5>
    <ul class="abs col-list" style="left:105px"><li>Home</li><li>About us</li><li>Kitchens</li><li>Bathrooms</li><li>Interior doors</li><li>Contact us</li></ul>
    <div class="abs divider" style="left:222px"></div>
    <h5 class="abs col-title" style="left:262px;font-weight:400">WHAT WE DO</h5>
    <ul class="abs col-list" style="left:262px;line-height:19.3px"><li>Value proposition</li><li>Our work</li><li>Testimonials</li><li>FAQ</li><li>Contact us</li></ul>
    <div class="abs divider" style="left:379px"></div>
    <h5 class="abs col-title" style="left:411px;font-weight:400">CONTACT US</h5>
    <p class="abs contact-copy">Nunc tempus felis vitae urna. Vivamus neque at volutpat rutrum, purus nisia tempus libero lectus</p>
    <p class="abs contact-lines"><b>E-MAIL:</b> INFO@HALVERNWEBWORKS.COM<br><b>PHONE:</b> 5550 100 200</p>
    <div class="abs divider" style="left:654px"></div>
    <h5 class="abs col-title" style="left:690px;font-weight:400">GET CONNECTED</h5>
    <ul class="abs social"><li><span></span>Friendlane</li><li><span></span>Chirpline</li><li><span></span>Workweb</li><li><span></span>RSS</li></ul>
    <div class="abs footer-base"></div>
    <p class="abs copyright">Copyright © 2014 Halvern Webworks. All rights reserved.</p>
  </footer>
</div>
</body>
</html>
```